Business Card Design Project

A business card for a new company in Ontario Canada called Build for Growth. It is a consulting company which uses Brixo as the medium for facilitation.

The target market is for senior leaders in healthcare and social services.

Industry/Entity Type

Healthcare

Requirements
Must have
• The name Build For Growth
Dana Montreuil RRT, B Ed (AD ed).
Tacticraft Facililitator (R)

Tag Line
Engaging Transforming and Innovative
The attached logo

danamontreuil@examplemail.com
416-555-0147
Should not have
• Lime green
Times New Roman or Arial font
Do not include Brixo bricks on the card.

```html
<!DOCTYPE html>
<html lang="en">
<head>
<meta charset="utf-8">
<title>Build For Growth – Business Card</title>
<link rel="stylesheet" href="https://fonts.googleapis.com/css2?family=Carlito:ital,wght@0,400;0,700;1,400&display=swap">
<style>
  :root {
    --page-bg: #ffffff;
    --card-bg: #e0e0e0;
    --ink: #1f1f1f;
    --ink-soft: #2a2a2a;
    --accent-purple: #5a1a6e;
    --rule: #ffffff;
    --brand-ink: #1a1a1a;
  }
  * { margin: 0; padding: 0; box-sizing: border-box; }
  html, body {
    width: 1200px; height: 1199px; overflow: hidden;
    background: var(--page-bg);
    font-family: "Carlito", "Calibri", sans-serif;
    color: var(--ink);
  }
  .canvas { position: relative; width: 1200px; height: 1199px; }
  .card {
    position: absolute; left: 184px; width: 800px; height: 454px;
    background: var(--card-bg);
  }
  .card--front { top: 104px; }
  .card--back { top: 620px; }

  .holder { position: absolute; left: 68px; top: 78px; }
  .holder__name { font-size: 24px; color: var(--ink-soft); white-space: nowrap; }
  .holder__name-main { color: var(--accent-purple); }
  .holder__role { margin-top: 10px; font-size: 21px; font-style: italic; }

  .contact { position: absolute; left: 68px; top: 205px; font-size: 18px; line-height: 29px; }

  .divider {
    position: absolute; left: 0; top: 280px; width: 504px; height: 3px;
    background: var(--rule);
  }

  .tagline {
    position: absolute; left: 280px; top: 312px; width: 242px;
    text-align: center; font-size: 29px; font-style: italic; line-height: 39px;
  }

  .brand {
    position: absolute; display: flex; flex-direction: column; align-items: center;
  }
  .brand--front { left: 556px; top: 34px; width: 240px; }
  .brand--back { left: 250px; top: 70px; width: 300px; }
  .brand__mark { background: var(--accent-purple); }
  .brand--front .brand__mark { width: 150px; height: 150px; }
  .brand--back .brand__mark { width: 200px; height: 200px; }
  .brand__name {
    margin-top: 30px; font-size: 24px; letter-spacing: 1px;
    text-transform: uppercase; color: var(--brand-ink); white-space: nowrap;
  }
  .brand--back .brand__name { margin-top: 44px; font-size: 26px; }
</style>
</head>
<body>
<main class="canvas">
  <section class="card card--front" aria-label="Card front">
    <div class="holder">
      <p class="holder__name"><span class="holder__name-main">Dana Montreuil</span> RRT, B Ed (AD ed).</p>
      <p class="holder__role">Tacticraft Facililitator (R)</p>
    </div>
    <div class="contact">
      <p>danamontreuil@examplemail.com</p>
      <p>416-555-0147</p>
    </div>
    <div class="divider"></div>
    <p class="tagline">Engaging Tansforming and Innovative</p>
    <div class="brand brand--front">
      <div class="brand__mark"></div>
      <p class="brand__name">Build For Growth</p>
    </div>
  </section>

  <section class="card card--back" aria-label="Card back">
    <div class="brand brand--back">
      <div class="brand__mark"></div>
      <p class="brand__name">Build For Growth</p>
    </div>
  </section>
</main>
</body>
</html>
```